Pagebook Ads for HOA Law Firm

We need to create certain ads for a Pagebook ads campaign. We are a law firm in Florida that represents homeowners against HOAs. We need to create the following ads:

1. Image Ads Specifications:

File Type: JPG or PNG
Ratio: 1.91:1 to 4:5
Resolution:
a) 1:1 ratio: 1080 x 1080 pixels
b) 4:5 ratio: 1080 x 1350 pixels
Maximum File Size: 30MB
Minimum Width: 600 pixels
Minimum Height:
a) 1:1 ratio: 600 pixels
b) 4:5 ratio: 750 pixels
Key Elements to Include in the Ads:

1) Headline: "HOA Violating Your Rights?"
2) Main Message: "We sue HOAs for Homeowners."
3) Firm Name: Lindqvist Harrow, P.A.
4) Website: www.covenantshieldcounsel.example
5) Phone Number: 1-800-555-0148
6) Florida Bar Compliance Statement: "Serving Homeowners in Florida with our main office in Miami-Dade."
7) Call-to-Action (CTA): Include a strong CTA such as “Contact us today for a consultation!”
8) Tone and Style: Professional yet approachable. The ad should emphasize trust, expertise, and our dedication to homeowners' rights.
9) Branding: Please use our firm's brand colors and fonts. Ensure that our logo is prominently placed within the ad.
10) Image Suggestions: Consider using images of Florida homes, frustrated homeowners, or visuals that evoke trust, protection, and legal authority.

```html
<!DOCTYPE html>
<html lang="en">
<head>
<meta charset="utf-8">
<title>HOA Violating Your Rights? – Ad Set</title>
<link href="https://fonts.googleapis.com/css2?family=Poppins:wght@400;500;600;700;800&display=swap" rel="stylesheet">
<style>
  :root {
    --board: #a3a3a3;
    --navy: #0f1580;
    --royal: #1b22a8;
    --white: #ffffff;
    --ice: #c9d6f5;
    --photo-warm-a: #6b5a4a;
    --photo-warm-b: #2e2620;
    --photo-team-a: #8fa4c8;
    --photo-team-b: #1d2550;
    --label: #ffffff;
  }
  * { box-sizing: border-box; margin: 0; padding: 0; }
  html, body {
    width: 682px; height: 1200px; overflow: hidden;
    background: var(--board);
    font-family: "Poppins", sans-serif;
  }
  .board { position: relative; width: 682px; height: 1200px; }

  .ad {
    position: absolute; left: 114px; width: 472px;
    background: var(--white); overflow: hidden;
  }
  .ad--square { top: 50px; height: 414px; }
  .ad--portrait { top: 643px; height: 443px; }

  .size-label {
    position: absolute; left: 0; width: 682px; text-align: center;
    color: var(--label); font-weight: 600; font-size: 19px; letter-spacing: .5px;
  }
  .size-label--square { top: 482px; }
  .size-label--portrait { top: 1106px; }

  .headline { position: absolute; left: 18px; color: var(--navy); font-weight: 800; line-height: .98; z-index: 2; }
  .headline__hoa { display: block; }
  .ad--square .headline { top: 8px; }
  .ad--square .headline__hoa { font-size: 40px; }
  .ad--square .headline__rest { font-size: 22px; display: block; }
  .ad--portrait .headline { top: 10px; }
  .ad--portrait .headline__hoa { font-size: 46px; }
  .ad--portrait .headline__rest { font-size: 24px; display: block; line-height: 1.08; }

  .band { position: absolute; left: 0; right: 0; bottom: 0; background: var(--royal); }
  .ad--square .band { top: 96px; }
  .ad--portrait .band { top: 126px; }

  .hero-photo {
    position: absolute; border-radius: 50%;
    border: 6px solid var(--royal);
    background: radial-gradient(circle at 45% 45%, var(--photo-warm-a), var(--photo-warm-b));
  }
  .ad--square .hero-photo { left: 244px; top: -60px; width: 256px; height: 256px; }
  .ad--portrait .hero-photo { left: 240px; top: -64px; width: 262px; height: 262px; }

  .tagline { position: absolute; left: 18px; color: var(--white); font-weight: 600; }
  .ad--square .tagline { top: 116px; font-size: 15px; }
  .ad--portrait .tagline { top: 144px; font-size: 16px; }

  .firm-name {
    position: absolute; left: 18px; display: flex; align-items: center; gap: 8px;
    color: var(--white); font-weight: 600;
  }
  .firm-name__dot { width: 12px; height: 12px; border-radius: 50%; background: var(--white); }
  .ad--square .firm-name { top: 176px; font-size: 15px; }
  .ad--portrait .firm-name { top: 204px; font-size: 15px; }

  .team-photo {
    position: absolute; left: 18px; width: 175px;
    border: 3px solid var(--ice);
    background: linear-gradient(180deg, var(--photo-team-a), var(--photo-team-b));
  }
  .ad--square .team-photo { top: 240px; height: 160px; border-radius: 10px; }
  .ad--portrait .team-photo { top: 262px; height: 184px; border-radius: 10px 10px 0 0; border-bottom: none; }

  .compliance {
    position: absolute; border: 1.5px solid var(--ice); border-radius: 6px;
    color: var(--white); font-size: 13px; line-height: 1.3; padding: 8px 14px 8px 20px;
  }
  .compliance strong { font-weight: 700; }
  .compliance__mark { position: absolute; font-size: 34px; font-weight: 700; line-height: 1; color: var(--white); }
  .compliance__mark--open { left: -10px; top: -10px; }
  .compliance__mark--close { right: -8px; bottom: -24px; }
  .ad--square .compliance { left: 234px; top: 200px; width: 214px; }
  .ad--portrait .compliance { left: 234px; top: 222px; width: 214px; }

  .contact { position: absolute; color: var(--white); }
  .ad--square .contact { left: 234px; top: 290px; }
  .ad--portrait .contact { left: 234px; top: 318px; }
  .contact__cta { font-size: 13px; font-weight: 500; line-height: 1.25; text-transform: uppercase; }
  .contact__cta strong { display: block; font-weight: 700; }
  .contact__line { display: flex; align-items: center; gap: 7px; font-size: 12.5px; margin-top: 10px; white-space: nowrap; }
  .contact__line--web { font-size: 10px; margin-top: 8px; }
  .contact__phone { font-weight: 600; font-size: 14px; }
  .icon { width: 15px; height: 15px; flex: none; }
</style>
</head>
<body>
<div class="board">

  <section class="ad ad--square">
    <div class="band"></div>
    <div class="hero-photo" role="img" aria-label="Photo of a worried homeowner couple reviewing papers at home"></div>
    <h1 class="headline"><span class="headline__hoa">HOA</span><span class="headline__rest">VIOLATING<br>YOUR RIGHTS?</span></h1>
    <p class="tagline">We sue HOAs for Homeowners.</p>
    <div class="firm-name"><span class="firm-name__dot"></span>Lindqvist Harrow, P.A.</div>
    <div class="team-photo" role="img" aria-label="Photo of the two firm attorneys in suits in front of a Florida home"></div>
    <div class="compliance">
      <span class="compliance__mark compliance__mark--open">&ldquo;</span>
      Serving Homeowners in Florida with our main office in <strong>Miami-Dade</strong>
      <span class="compliance__mark compliance__mark--close">&rdquo;</span>
    </div>
    <div class="contact">
      <p class="contact__cta">Contact us today<strong>for a consultation</strong></p>
      <p class="contact__line">
        <svg class="icon" viewBox="0 0 16 16"><circle cx="8" cy="8" r="8" fill="#fff"/><path d="M5.2 4.2l1.4-.2.8 1.9-.9.8a5 5 0 0 0 2.8 2.8l.8-.9 1.9.8-.2 1.4c-3.8.3-6.9-2.8-6.6-6.6z" fill="#1b22a8"/></svg>
        <span class="contact__phone">1-800-555-0148</span>
      </p>
      <p class="contact__line contact__line--web">
        <svg class="icon" viewBox="0 0 16 16"><circle cx="8" cy="8" r="8" fill="#fff"/><circle cx="8" cy="8" r="4.6" fill="none" stroke="#1b22a8" stroke-width="1"/><ellipse cx="8" cy="8" rx="2" ry="4.6" fill="none" stroke="#1b22a8" stroke-width="1"/><path d="M3.4 8h9.2" stroke="#1b22a8" stroke-width="1"/></svg>
        www.covenantshieldcounsel.example
      </p>
    </div>
  </section>
  <p class="size-label size-label--square">1080*1080</p>

  <section class="ad ad--portrait">
    <div class="band"></div>
    <div class="hero-photo" role="img" aria-label="Photo of a worried homeowner couple reviewing papers at home"></div>
    <h2 class="headline"><span class="headline__hoa">HOA</span><span class="headline__rest">VIOLATING<br>YOUR RIGHTS?</span></h2>
    <p class="tagline">We sue HOAs for Homeowners.</p>
    <div class="firm-name"><span class="firm-name__dot"></span>Lindqvist Harrow, P.A.</div>
    <div class="team-photo" role="img" aria-label="Photo of the two firm attorneys in suits in front of a Florida home"></div>
    <div class="compliance">
      <span class="compliance__mark compliance__mark--open">&ldquo;</span>
      Serving Homeowners in Florida with our main office in <strong>Miami-Dade</strong>
      <span class="compliance__mark compliance__mark--close">&rdquo;</span>
    </div>
    <div class="contact">
      <p class="contact__cta">Contact us today<strong>for a consultation</strong></p>
      <p class="contact__line">
        <svg class="icon" viewBox="0 0 16 16"><circle cx="8" cy="8" r="8" fill="#fff"/><path d="M5.2 4.2l1.4-.2.8 1.9-.9.8a5 5 0 0 0 2.8 2.8l.8-.9 1.9.8-.2 1.4c-3.8.3-6.9-2.8-6.6-6.6z" fill="#1b22a8"/></svg>
        <span class="contact__phone">1-800-555-0148</span>
      </p>
      <p class="contact__line contact__line--web">
        <svg class="icon" viewBox="0 0 16 16"><circle cx="8" cy="8" r="8" fill="#fff"/><circle cx="8" cy="8" r="4.6" fill="none" stroke="#1b22a8" stroke-width="1"/><ellipse cx="8" cy="8" rx="2" ry="4.6" fill="none" stroke="#1b22a8" stroke-width="1"/><path d="M3.4 8h9.2" stroke="#1b22a8" stroke-width="1"/></svg>
        www.covenantshieldcounsel.example
      </p>
    </div>
  </section>
  <p class="size-label size-label--portrait">1080*1350</p>

</div>
</body>
</html>
```